LABEL DESIGN NEEDED FOR Mabel Fernwood Cookies

I am starting a Cookie Company with my daughter Mabel that will begin by making chocolate chip cookies.
These labels will go on a 2.5 by 2x6 clear cellophane bag that we will use to give out samples of our cookies to others to introduce our new- company to them.
I want the label to be 2X3 for both the front and the back.
These labels are for a cookie business starting out by making chocolate chip cookies. We will start out using clear cellophane bags with gold twist ties.
The size of the bags we will be using at first are 2.5x2x6 and 3.5x2x7.5.
Again, the clear cellophane bags will contain chocolate chip cookies that are round and weigh 1.5 oz. each.
On the front of the label I want it to have my logo which says Mabel Fernwood Cookies (see attached) with the name of the cookie (Chocolate Chip) and the weight (3oz.)
On the back of the label I would like the following:
Ingredients: All-purpose Flour, Semisweet Chocolate Chips, Granulated Sugar, Light Brown Sugar, Butter, Egg yolk, Light Corn Syrup, Milk, Vanilla Extract, Baking Soda, Salt
We also need it to say:
These products were manufactured in a facility that processes nuts and other known allergens. i.e. Milk, Eggs, Wheat, Soy
and it needs to have my address:
Cedarhaven, Maine 11942
I have attached three things which will help the artist:
1.Our company logo (Mabel Fernwood Cookies)
2.A front and back label of a packaging from a cookie company that I really liked and thought was very cute. This should give the artist a start in terms of what direction to head in.
Thank you so much for all your help and just let me know what I need to do next.

```html
<!DOCTYPE html>
<html lang="en">
<head>
<meta charset="utf-8">
<title>Mabel Fernwood Cookies – Chocolate Chip Label</title>
<link href="https://fonts.googleapis.com/css2?family=Courgette&family=Arimo:wght@400;700&display=swap" rel="stylesheet">
<style>
  :root {
    --backdrop: #2b2b2b;
    --label-red: #a3162d;
    --label-red-dark: #8c1024;
    --cream: #fdeac4;
    --cocoa: #3e1a0e;
    --ink: #111111;
    --cookie-light: #e2b27a;
    --cookie-dark: #6b3a1c;
  }
  * { margin: 0; padding: 0; box-sizing: border-box; }
  html, body {
    width: 1200px; height: 1000px; overflow: hidden;
    background: var(--backdrop);
  }
  .canvas { position: relative; width: 1200px; height: 1000px; }

  .label {
    position: absolute; left: 286px; width: 628px; height: 418px;
    background: var(--label-red);
  }
  .label--front { top: 60px; }
  .label--back { top: 508px; }

  /* front */
  .front-panel {
    position: absolute; left: 32px; top: 30px; width: 562px; height: 298px;
    background: var(--cream); border-radius: 34px;
  }
  .front-panel__dots {
    position: absolute; inset: 10px;
    border: 5px dotted var(--label-red); border-radius: 26px;
  }
  .brand-tab {
    position: absolute; left: 19px; top: 18px; width: 236px; height: 82px;
    background: var(--cream); border: 4px solid var(--label-red-dark);
    border-radius: 30px;
    display: flex; align-items: center; justify-content: center; gap: 8px;
  }
  .brand-tab__dot {
    width: 10px; height: 10px; border-radius: 50%; background: var(--cocoa);
  }
  .brand-tab__name {
    font-family: 'Arimo', Arial, sans-serif; font-size: 15px; font-weight: 400;
    color: var(--cocoa); letter-spacing: 0.5px;
  }
  .product-title {
    position: absolute; left: 0; width: 628px; top: 110px; text-align: center;
    font-family: 'Courgette', cursive; font-weight: 400; line-height: 1;
  }
  .product-title__flavor { display: block; font-size: 56px; color: var(--cocoa); }
  .product-title__kind { display: block; font-size: 60px; color: var(--label-red); margin-top: 10px; }
  .net-weight {
    position: absolute; left: 421px; top: 284px;
    font-family: 'Arimo', Arial, sans-serif; font-size: 20px; color: var(--ink);
  }
  .cookie-art {
    position: absolute; left: 206px; top: 262px; width: 210px; height: 118px;
    border-radius: 50% 50% 45% 45%;
    background: radial-gradient(ellipse at 50% 40%, var(--cookie-light) 0%, #c98e52 55%, var(--cookie-dark) 100%);
  }

  /* back */
  .back-panel {
    position: absolute; left: 22px; top: 19px; width: 580px; height: 379px;
    background: var(--cream); border-radius: 40px;
    font-family: 'Arimo', Arial, sans-serif; font-size: 23px; line-height: 28px; color: var(--ink);
  }
  .ingredients { position: absolute; left: 33px; top: 12px; width: 530px; }
  .ingredients__heading { font-weight: 700; font-size: 21px; }
  .allergen-note { position: absolute; left: 27px; top: 160px; width: 545px; }
  .contact { position: absolute; left: 33px; top: 312px; }
</style>
</head>
<body>
<main class="canvas">
  <section class="label label--front" aria-label="Front label">
    <div class="front-panel"><div class="front-panel__dots"></div></div>
    <div class="brand-tab">
      <span class="brand-tab__dot"></span>
      <span class="brand-tab__name">Mabel Fernwood Cookies</span>
    </div>
    <h1 class="product-title">
      <span class="product-title__flavor">Chocolate Chip</span>
      <span class="product-title__kind">Cookies</span>
    </h1>
    <div class="cookie-art" role="img" aria-label="Illustration of two chocolate chip cookies"></div>
    <p class="net-weight">NET WT: 3 oz</p>
  </section>

  <section class="label label--back" aria-label="Back label">
    <div class="back-panel">
      <p class="ingredients"><span class="ingredients__heading">Ingredients:</span><br>
        All-purpose Flour, Semisweet Chocolate Chips, Granulated Sugar, Light Brown Sugar, Butter, Egg yolk, Light Corn Syrup, Milk, Vanilla Extract, Baking Soda, Salt</p>
      <p class="allergen-note">These products were manufactured in a facility that processes nuts and other known allergens.<br>i.e. Milk, Eggs, Wheat, Soy</p>
      <p class="contact">Your Phone Number<br>Cedarhaven, Maine 11942</p>
    </div>
  </section>
</main>
</body>
</html>
```